Top New England Restaurant Needs Website Redesign

We currently have a website, rmsbistro.com, but would like to redesign it. We are a casual upscale restaurant specializing in breakfast and lunch. We are one of the top rated restaurants in all of New England and would like our site to look like it as well. We'd love to have a blog/news section that will be updated weekly or so, as well as an email capture feature on the page.

The site will mostly be static, with lots of pictures (I'll take them and provide). The only part of the site that will get updated regularly is the blog and/or news (could be the same page).

Some restaurant websites I like are: www.corvintable.com, www.brassandoat.com,

Target Market(s)

Foodies, RM's Bistro customers,

Industry/Entity Type

Restaurant

Logo Text

RM's Bistro

Font styles to use
Sans Serif

Requirements
Must have
• Friendloop Like Box, Dinetip Box, Email capture, Blog/News, About Us page, Contact page

```html
<!DOCTYPE html>
<html lang="en">
<head>
<meta charset="utf-8">
<title>RM's Bistro</title>
<link rel="stylesheet" href="https://fonts.googleapis.com/css2?family=Bebas+Neue&family=Oswald:wght@200;300;500;600&display=swap">
<style>
  :root {
    --page-grey: #959495;
    --card-white: #ffffff;
    --ink: #111111;
    --ink-soft: #2e2e2e;
    --hero-top: #f3efe8;
    --hero-mid: #d9b892;
    --hero-bottom: #b89a78;
    --white: #ffffff;
  }
  * { margin: 0; padding: 0; box-sizing: border-box; }
  html, body { width: 859px; height: 1200px; overflow: hidden; }
  body {
    position: relative;
    background: var(--page-grey);
    font-family: "Oswald", "Arial Narrow", sans-serif;
  }
  .hero {
    position: absolute; left: 0; top: 0; width: 859px; height: 604px;
    background: linear-gradient(180deg, var(--hero-top) 0%, var(--hero-mid) 55%, var(--hero-bottom) 100%);
  }
  .menu-toggle { position: absolute; left: 782px; top: 46px; }
  .brand {
    position: absolute; right: 47px; top: 262px;
    font-family: "Bebas Neue", "Oswald", sans-serif;
    font-weight: 400;
    font-size: 90px; line-height: 1; color: var(--white);
    letter-spacing: 1px;
  }
  .hours {
    position: absolute; right: 47px; top: 358px;
    text-align: right; color: var(--white);
    font-weight: 300; font-size: 17px; line-height: 30px;
    letter-spacing: 5.5px; text-transform: uppercase;
  }
  .about-card {
    position: absolute; left: 62px; top: 680px; width: 734px; height: 450px;
    background: var(--card-white);
    box-shadow: 0 12px 30px rgba(0,0,0,.25);
  }
  .about-text {
    position: absolute; left: 148px; top: 159px; width: 453px;
    font-weight: 200; font-size: 12.5px; line-height: 22.8px;
    letter-spacing: 3.5px; color: var(--ink-soft); text-transform: uppercase;
  }
  .about-line {
    display: block; white-space: nowrap;
    text-align: justify; text-align-last: justify;
    margin-right: -3.5px;
  }
  .about-closing { display: flex; justify-content: space-between; white-space: nowrap; }
  .menu-link {
    color: var(--ink); font-weight: 500; letter-spacing: 4px;
    text-decoration: none; font-size: 13px; margin-right: -4px;
  }
  .section-dots { position: absolute; left: 822px; top: 840px; }
</style>
</head>
<body>
  <header class="hero" role="img" aria-label="Hero photograph of a signature dish served at the restaurant"></header>
  <svg class="menu-toggle" width="30" height="20" viewBox="0 0 30 20" aria-label="Menu">
    <rect x="0" y="1" width="30" height="2.6" fill="#111"/>
    <rect x="0" y="8" width="30" height="2.6" fill="#111"/>
    <rect x="0" y="15" width="30" height="2.6" fill="#111"/>
  </svg>
  <h1 class="brand">RM'S BISTRO</h1>
  <div class="hours">Tue. thru Sunday<br>From 7 a.m to 3p.m</div>

  <section class="about-card">
    <div class="about-text">
      <span class="about-line">RM's Bistro is committed to superior food quality</span>
      <span class="about-line">and cultivating a pleasurable and welcoming</span>
      <span class="about-line">dining experience, akin to enjoying a home-cooked</span>
      <span class="about-line">meal. We are truly excited to bring a fresh,</span>
      <span class="about-line">new restaurant for breakfast and lunch to the</span>
      <div class="about-closing"><span>City of champions.</span><a class="menu-link" href="#">Discover our menu</a></div>
    </div>
  </section>

  <svg class="section-dots" width="14" height="140" viewBox="0 0 14 140" aria-label="Section navigation">
    <circle cx="7" cy="8" r="4.6" fill="none" stroke="#111" stroke-width="2.6"/>
    <circle cx="7" cy="38" r="1.8" fill="#111"/>
    <circle cx="7" cy="69" r="1.8" fill="#111"/>
    <circle cx="7" cy="100" r="1.8" fill="#111"/>
    <circle cx="7" cy="132" r="1.8" fill="#111"/>
  </svg>
</body>
</html>
```